Non-profit sports organization needs templates for Word and InDesign

"Pelo Minis" is a non-profit organization in Winterthur, which supports the recruitment of young talent by the handball clubs in Winterthur. Every year we run several camps, a tournament for schoolchildren and several handball lessons at school.
During these activities there are always written information. So far we have not given much thought to the design. But since we think that a professional design will also lead to more interaction, we now turn to you as a designer.

For the communication with partners, sponsors, patrons, etc. we need a uniform appearance. Since different departments are currently working with different programs, we need a template for letters and documentation for Word and InDesign.

We will need the documentation template for project descriptions, information, etc.
The letter templates are needed to contact sponsors, authorities, patrons, etc.

Both the letter template and the documentation template should look modern. The design should be based on the existing flyers. Otherwise we have no other requirements so far.

Homepage: www.pelo-minis.ch

Target Market(s)

Letters, documentation or information to authorities, sponsors, associations, patrons, members, participants, etc.

Requirements
Must have
• In addition to the design, the templates should also contain a concept for titles, paragraphs, lists, etc. (colors / fonts / ...)

Word and Indesign templates

```html
<!DOCTYPE html>
<html lang="en">
<head>
<meta charset="utf-8">
<title>Pelo Minis – Letterhead</title>
<link rel="stylesheet" href="https://fonts.googleapis.com/css2?family=Montserrat:wght@400;500;700&display=swap">
<style>
  :root {
    --brand-red: #e3141b;
    --brand-red-dark: #c70f16;
    --brand-blue: #1f5fd6;
    --text-grey: #7d8a88;
    --paper: #ffffff;
  }
  * { margin: 0; padding: 0; box-sizing: border-box; }
  html, body { width: 857px; height: 1200px; overflow: hidden; background: var(--paper); }
  body { font-family: "Montserrat", Arial, sans-serif; }

  .letterhead { position: relative; width: 857px; height: 1200px; overflow: hidden; background: var(--paper); }

  .header-band, .footer-band { position: absolute; left: 0; width: 857px; }
  .header-band { top: 0; height: 160px; }
  .footer-band { top: 1100px; height: 100px; }

  .brand {
    position: absolute; left: 72px; top: 50px;
    display: flex; align-items: center; gap: 12px;
    color: var(--paper); font-weight: 700; font-size: 30px; letter-spacing: 0.5px;
  }
  .brand-dot { width: 34px; height: 34px; border-radius: 50%; background: var(--paper); }

  .header-url {
    position: absolute; right: 28px; top: 98px;
    color: var(--paper); font-weight: 700; font-size: 21px;
  }

  .letter-body { position: absolute; left: 74px; top: 262px; width: 712px; color: var(--text-grey); }
  .headline { color: var(--brand-red); font-weight: 700; font-size: 37px; line-height: 1; margin-bottom: 16px; }
  .subhead { color: var(--brand-red); font-weight: 700; font-size: 23px; line-height: 1; margin: 46px 0 10px; }
  .letter-body p { font-size: 14.2px; line-height: 26.5px; margin-bottom: 26px; }

  .sign-off { position: absolute; left: 600px; top: 912px; color: var(--text-grey); font-size: 15px; line-height: 25px; }
  .sign-off .signer { margin-top: 52px; }

  .footer-url {
    position: absolute; left: 0; top: 1138px; width: 857px; height: 62px;
    display: flex; align-items: center; justify-content: center;
    color: var(--paper); font-weight: 700; font-size: 20px;
  }
</style>
</head>
<body>
<main class="letterhead">
  <svg class="header-band" viewBox="0 0 857 160" aria-hidden="true">
    <path d="M0 0 H857 V70 C700 70 520 72 420 100 C370 115 330 140 250 156 H0 Z" fill="var(--brand-red)"/>
    <path d="M857 80 V140 H400 C440 110 520 86 857 80 Z" fill="var(--brand-red)"/>
    <path d="M400 140 C450 120 520 112 857 112 V140 Z" fill="var(--brand-blue)"/>
    <path d="M560 0 L857 0 L857 40 C760 20 660 12 560 0 Z" fill="var(--brand-red-dark)" opacity="0.35"/>
  </svg>

  <div class="brand"><span class="brand-dot"></span>Pelo Minis</div>
  <div class="header-url">www.pelo-minis.ch</div>

  <section class="letter-body">
    <h1 class="headline">YOUR HEADLINE</h1>
    <p>Duis autem vel eum iriure dolor in hendrerit in vulputate velit esse molestie consequat, vel illum dolore eu feugiat nulla facilisis at vero eros et accumsan et iusto odio dignissim qui blandit praesent luptatum zzril delenit augue duis dolore te feugait nulla facilisi.</p>
    <p>Lorem ipsum dolor sit amet, cons ectetuer adipiscing elit, sed diam nonummy nibh euismod tincidunt ut laoreet dolore magna aliquam erat volutpat.</p>
    <h2 class="subhead">YOUR TEXT HERE</h2>
    <p>Lorem ipsum dolor sit amet, consectetuer adipiscing elit, sed diam nonummy nibh euismod tincidunt ut laoreet dolore magna aliquam erat volutpat. Ut wisi enim ad minim veniam, quis nostrud exerci tation ullamcorper suscipit lobortis nisl ut aliquip ex ea commodo consequat. Duis autem vel eum iriure dolor in hendrerit in vulputate velit esse molestie consequat, vel illum dolore eu feugiat nulla facilisis at vero eros et accumsan et iusto odio dignissim qui blandit praesent luptatum zzril delenit augue duis dolore te feugait nulla facilisi.</p>
    <p>Vel illum dolore eu feugiat nulla facilisis at vero eros et accumsan et iusto odio dignissim qui blandit praesent luptatum zzril delenit augue duis dolore te feugait nulla facilisi.</p>
  </section>

  <div class="sign-off">
    <div>Regard</div>
    <div class="signer">Martina<br>Art Director</div>
  </div>

  <svg class="footer-band" viewBox="0 0 857 100" aria-hidden="true">
    <path d="M0 10 H795 A10 10 0 0 1 805 20 V24 H0 Z" fill="var(--brand-blue)"/>
    <rect x="0" y="38" width="857" height="62" fill="var(--brand-red)"/>
  </svg>
  <div class="footer-url">www.pelo-minis.ch</div>
</main>
</body>
</html>
```